Three different companies capability statement

We are three companies looking to create one capability statement that combines all of our companies' capabilities into one 4-page brochure (for back and front printing). One company does not have one but we are providing all the companies' websites to be able to pull information from each. This capability statement is what will provide companies interested in working with us.
Company order: KTR, Bellmont, Brightwell
Please look through the pages of our sites:
This company does not have a capability statement yet to include Brightwell Partners, LLC. Please use this company’s contracted service and about me page, more than information about the tutoring services offered: https://brightwellstudyhub.example/
These two are attached in the brief
https://www.ktrsolutions.example/
https://bmxllcforward.example/

Please ask any questions you might have.
I created an example of information using ChatGPT and our websites. This does not need to be used. Just an example

Target Market(s)

Businesses who want to hire us

Industry/Entity Type

Contract work

Requirements
Must have
• All three companies logos, information for all three companies. NAICS codes. Some client partners. Certifications
Nice to have
• We like the one we uploaded that has 2- 4 pages
Should not have
• Pictures of owners

```html
<!DOCTYPE html>
<html lang="en">
<head>
<meta charset="utf-8">
<title>KTR · Bellmont · Brightwell — Company Capability Statement</title>
<link href="https://fonts.googleapis.com/css2?family=Poppins:wght@400;500;600;700&display=swap" rel="stylesheet">
<style>
  :root{
    --backdrop:#e8e5e0;
    --paper:#f6f3ea;
    --paper-cool:#eef3f5;
    --teal:#2bb3d0;
    --teal-light:#5fd0e2;
    --teal-deep:#1e9cc0;
    --ink:#2f3a42;
    --ink-soft:#4a5660;
    --slate:#5d7080;
    --white:#ffffff;
  }
  *{box-sizing:border-box;margin:0;padding:0}
  html,body{width:1200px;height:900px;overflow:hidden}
  body{background:var(--backdrop);font-family:'Poppins',sans-serif;color:var(--ink);position:relative}

  .page{position:absolute;top:185px;width:375px;height:530px;overflow:hidden;box-shadow:0 4px 14px rgba(0,0,0,.12)}

  /* ---------- Cover ---------- */
  .cover{left:30px;background:linear-gradient(180deg,#dfe8ec 0%,#eef1ef 40%,#f4f1e6 60%,#eef0ee 100%)}
  .cover-eyebrow{position:absolute;top:80px;width:100%;text-align:center;font-size:12px;letter-spacing:5px;color:var(--slate);font-weight:500}
  .cover-title{position:absolute;top:102px;width:100%;text-align:center;font-size:25px;font-weight:700;color:var(--slate);letter-spacing:.3px}
  .cover-brands{position:absolute;top:160px;width:100%;display:flex;justify-content:center;gap:22px;align-items:center}
  .brand{display:flex;align-items:center;gap:4px;font-size:10px;font-weight:600;color:var(--teal-deep)}
  .brand-dot{width:9px;height:9px;border-radius:50%;background:var(--teal)}
  .brand.is-grey{color:#8c8f92}
  .brand.is-grey .brand-dot{background:#b5b7b9}
  .cover-photo{position:absolute;left:0;right:0;bottom:0;height:225px;background:linear-gradient(180deg,rgba(238,240,238,0) 0%,#b9cfdc 35%,#8fb0c6 70%,#7d9fb8 100%)}

  /* ---------- Spread ---------- */
  .inside-left{left:425px;background:linear-gradient(180deg,var(--paper-cool) 0%,var(--paper) 100%)}
  .inside-right{left:800px;background:linear-gradient(180deg,#f3f1e8 0%,var(--paper) 100%);box-shadow:4px 4px 14px rgba(0,0,0,.12)}
  .top-band{position:absolute;top:0;left:0;right:0;height:40px;background:linear-gradient(90deg,var(--teal) 0%,var(--teal-light) 100%)}
  .inside-right .top-band{right:70px;height:36px;background:linear-gradient(90deg,var(--teal-light) 0%,#a6e0ea 70%,rgba(166,224,234,0) 100%)}

  .intro-card{position:absolute;top:26px;left:10px;width:202px;height:84px;background:var(--white);border:1.2px solid var(--teal);border-radius:0 0 8px 0;padding:6px 8px;font-size:6.4px;line-height:1.5;color:var(--ink-soft)}
  .masthead{position:absolute;top:40px;left:236px;display:flex;align-items:center;gap:5px;font-size:17px;font-weight:700;color:var(--teal-deep)}
  .masthead .brand-dot{width:13px;height:13px}

  .section-title{font-size:9.5px;font-weight:700;color:var(--ink);letter-spacing:.2px}
  .section-title.is-teal{color:var(--teal-deep);text-align:center}
  .tagline{font-size:6px;font-weight:500;color:var(--teal-deep);margin-top:1px}
  .body-copy{font-size:6.3px;line-height:1.55;color:var(--ink-soft)}

  .glance{position:absolute;top:118px;left:12px;right:12px}
  .glance .body-copy{margin-top:5px}
  .point-list{list-style:none;margin-top:3px}
  .point-list li{display:flex;gap:5px;font-size:6.3px;line-height:1.5;color:var(--ink-soft);margin-bottom:3px}
  .point-list li svg{flex:0 0 9px;margin-top:1px}
  .plain-list{list-style:none;margin-top:4px}
  .plain-list li{font-size:6.3px;line-height:1.5;color:var(--ink-soft);margin-bottom:3px;padding-left:14px}

  .naics{position:absolute}
  .naics-bar{margin-top:4px;border-radius:8px;background:linear-gradient(90deg,var(--teal-light),var(--teal));padding:3px 12px;font-size:8.3px;line-height:1.3;color:var(--white);text-align:center;letter-spacing:.2px}
  .inside-left .naics{top:360px;left:12px;right:8px}
  .inside-right .naics{top:440px;left:12px;right:12px}

  .performance{position:absolute;top:418px;left:12px;width:205px}
  .performance .section-title{color:var(--teal-deep)}
  .partner-box{margin-top:5px;height:80px;border:1.2px solid var(--teal-light);border-radius:0 8px 8px 0;padding:7px 8px;display:grid;grid-template-columns:1fr 1fr 1fr;grid-template-rows:1fr 1fr;gap:6px 6px;align-items:center}
  .partner{font-size:7px;font-weight:600;color:var(--ink-soft);text-align:center;line-height:1.15}
  .seal-row{display:flex;gap:5px;justify-content:center;align-items:center}
  .seal{width:20px;height:20px;border-radius:50%;background:#c9d3dc}

  .certs{position:absolute;top:418px;left:228px;right:10px}
  .certs .section-title{color:var(--teal-deep)}
  .cert-list{list-style:none;margin-top:4px}
  .cert-list li{display:flex;gap:4px;font-size:6.2px;line-height:1.35;color:var(--ink-soft);margin-bottom:4.5px}
  .cert-list li::before{content:"";flex:0 0 6px;height:6px;margin-top:1px;border-radius:50%;background:var(--teal);box-shadow:0 0 0 1.5px #bfe9f1}

  .right-intro{position:absolute;top:18px;left:12px;width:245px}
  .right-about{position:absolute;top:92px;left:12px;right:18px}
  .corner-brand{position:absolute;top:22px;right:14px;flex-direction:column;gap:2px;font-size:9px}
  .corner-brand .brand-dot{width:22px;height:22px}

  .services{position:absolute;top:170px;left:12px;right:12px}
  .service-cols{display:grid;grid-template-columns:1fr 1fr;gap:0 12px;margin-top:6px}
  .service-cols ul{list-style:none}
  .service-cols li{display:flex;gap:4px;font-size:6.2px;line-height:1.4;color:var(--ink-soft);margin-bottom:3.2px}
  .service-cols li::before{content:"›";color:var(--teal);font-weight:700;font-size:8px;line-height:1}
  .service-cols .is-bold li{font-weight:500;color:var(--ink)}

  .industries{position:absolute;top:308px;left:12px;right:12px}
  .tile-row{display:flex;gap:8px;margin-top:6px}
  .tile{width:71px;height:71px;border-radius:5px;background:linear-gradient(180deg,var(--teal-light),var(--teal));display:flex;flex-direction:column;align-items:center;justify-content:space-between;padding:9px 3px 5px;color:var(--white);font-size:5.6px;line-height:1.2;text-align:center}
  .tile svg{width:32px;height:32px}

  .company-info{position:absolute;top:492px;left:12px;right:12px}
  .company-info .section-title{color:var(--teal-deep)}
  .id-row{display:flex;justify-content:space-between;margin-top:3px;font-size:6px;color:var(--ink-soft)}
  .id-row b{font-weight:600;color:var(--ink)}
</style>
</head>
<body>

  <!-- Cover -->
  <section class="page cover">
    <p class="cover-eyebrow">COMPANY</p>
    <h1 class="cover-title">CAPABILITY STATEMENT</h1>
    <div class="cover-brands">
      <span class="brand"><span class="brand-dot"></span>KTR</span>
      <span class="brand is-grey"><span class="brand-dot"></span>Bellmont</span>
      <span class="brand"><span class="brand-dot"></span>Brightwell</span>
    </div>
    <div class="cover-photo" role="img" aria-label="Upward view of glass office towers against a pale sky"></div>
  </section>

  <!-- Inside left -->
  <section class="page inside-left">
    <div class="top-band"></div>
    <div class="intro-card">Lorem ipsum dolor sit amet, consectetuer adipiscing elit, sed diam nonummy nibh euismod tincidunt ut laoreet dolore magna aliquam erat volutpat. Ut wisi enim ad minim veniam, quis nostrud exerci tation ullamcorper suscipit lobortis nisl ut aliquip ex ea commodo consequat. Duis autem vel eum iriure dolor in hendrerit</div>
    <div class="masthead"><span class="brand-dot"></span>KTR</div>

    <div class="glance">
      <h2 class="section-title">KTR PMO AT GLANCE</h2>
      <p class="tagline">Standardizing and Introducing Economics of Repetition in the Execution of Projects</p>
      <p class="body-copy">Lorem ipsum dolor sit amet, consectetuer adipiscing elit, sed diam nonummy nibh euismod tincidunt ut laoreet dolore magna aliquam erat volutpat. Ut wisi enim ad minim veniam, quis nostrud exerci tation ullamcorper suscipit lobortis nisl ut aliquip ex ea commodo consequat. Duis autem vel eum iriure dolor in hendrerit in vulputate velit esse molestie consequat, vel</p>
      <ul class="point-list">
        <li><svg viewBox="0 0 10 10" width="9" height="9"><circle cx="5" cy="5" r="5" fill="#2bb3d0"/><path d="M4 2.8 6.4 5 4 7.2" stroke="#fff" stroke-width="1.3" fill="none"/></svg>Lorem ipsum dolor sit amet, consectetuer adipiscing elit, sed diam nonummy nibh euismod tincidunt ut laoreet dolore magna aliquam erat volutpat. Ut wisi enim ad minim</li>
        <li><svg viewBox="0 0 10 10" width="9" height="9"><circle cx="5" cy="5" r="5" fill="#2bb3d0"/><path d="M4 2.8 6.4 5 4 7.2" stroke="#fff" stroke-width="1.3" fill="none"/></svg>Lorem ipsum dolor sit amet, conssuscipqesent luptatum zzril delenit augue duis dolore te feugait nulla facilisi.</li>
      </ul>
      <ul class="plain-list">
        <li>Lorem ipsum dolor sit amet, aliquiat nulla facilisis at vero eros et accumsan et iusto odio</li>
        <li>Lorem ipsum dolor sit amet, heniusto odio dignissim qui blandit praesent luptatum zzril delenit augue duis dolore te feugait nulla facilisi.</li>
        <li>Lorem ipsum dolor sit arat volutpat. Ut wisi enim ad minim veniam, quis nostrud exerci tation ullamcorper suscipit lobortis nisl ut aliquip ex ea commodo consequat.</li>
        <li>Lorem ipsum dolor sit amet, cam erat volutpat. Ut wisi enim ad minim veniam, quis nostrud exerci tation ullamcorper suscipit lobortis nisl ut aliquip ex ea commodo</li>
      </ul>
    </div>

    <div class="naics">
      <h3 class="section-title is-teal">NAICS Codes</h3>
      <div class="naics-bar">561210 &nbsp;•&nbsp; 561210 &nbsp;•&nbsp; 561210 &nbsp;•&nbsp; 561210 &nbsp;•&nbsp; 561210 &nbsp;•&nbsp; 561210<br>561210 &nbsp;•&nbsp; 561210 &nbsp;•&nbsp; 561210 &nbsp;•&nbsp; 561210 &nbsp;•&nbsp; 561210 &nbsp;•&nbsp; 561210</div>
    </div>

    <div class="performance">
      <h3 class="section-title">Past Performance</h3>
      <div class="partner-box">
        <span class="partner">Halvorsen Controls</span>
        <span class="partner">Northstream Water</span>
        <span class="partner">Crestline Realty</span>
        <span class="seal-row"><span class="seal"></span><span class="seal"></span></span>
        <span class="seal-row"><span class="seal"></span></span>
        <span class="partner">Regional Relief Agency</span>
      </div>
    </div>

    <div class="certs">
      <h3 class="section-title">Certifications</h3>
      <ul class="cert-list">
        <li>CCR &amp; OCRA Compliants (SAMS)</li>
        <li>Veteran Owned Business (VOB)</li>
        <li>Marlow County Minority Business Enterprise (MBE)</li>
        <li>Redfield County Water Authority (SLBE)</li>
        <li>Small Business</li>
      </ul>
    </div>
  </section>

  <!-- Inside right -->
  <section class="page inside-right">
    <div class="top-band"></div>
    <p class="right-intro body-copy">Lorem ipsum dolor sit amet, consectetuer adipiscing elit, sed diam nonummy nibh euismod tincidunt ut laoreet dolore magna aliquam erat volutpat. Ut wisi enim ad minim veniam, quis nostrud exerci tation ullamcorper suscipit lobortis</p>
    <span class="brand is-grey corner-brand"><span class="brand-dot"></span>Bellmont</span>
    <p class="right-about body-copy">Lorem ipsum dolor sit amet, consectetuer adipiscing elit, sed diam nonummy nibh euismod tincidunt ut laoreet dolore magna aliquam erat volutpat. Ut wisi enim ad minim veniam, quis nostrud exerci tation ullamcorper suscipit lobortis nisl ut aliquip ex ea commodo consequat. Duis autem vel eum iriure dolor in hendrerit in vulputate velit esse molestie consequat, vel illum dolore eu feugiat nulla facilisis at vero eros et accumsan et iusto odio dignissim qui blandit praesent luptatum zzril delenit augue</p>

    <div class="services">
      <h2 class="section-title">SERVICES</h2>
      <div class="service-cols">
        <ul>
          <li>Lorem ipsum dolor sit amet, consectetuer adipiscing elit, sed diam</li>
          <li>Lorem ipsum dolor sit amet, consec-</li>
          <li>Lorem ipsum dolor sit amet, consec-</li>
          <li>Lorem ipsum dolor sit amet, consec-</li>
          <li>Lorem ipsum dolor sit amet, consec-</li>
          <li>Lorem ipsum dolor sit amet, consectetuer adipiscing elit, sed diam</li>
        </ul>
        <ul class="is-bold">
          <li>Lorem ipsum dolor sit amet, consectetuer</li>
          <li>Lorem ipsum</li>
          <li>Lorem ipsum dolor sit amet</li>
          <li>Consectetuer adipiscing elit</li>
          <li>Sed diam nonummy nibh euismod</li>
          <li>Nonummy nibh euismod tincidunt ut laoreet dolore magna aliquam erat</li>
        </ul>
      </div>
    </div>

    <div class="industries">
      <h2 class="section-title">INDUSTRY CATEGORIES</h2>
      <div class="tile-row">
        <div class="tile">
          <svg viewBox="0 0 32 32" fill="none" stroke="#fff" stroke-width="1.6"><rect x="3" y="5" width="26" height="17" rx="1.5"/><path d="M16 22v5M10 27h12"/></svg>
          <span>Tech/Computer Sciences</span>
        </div>
        <div class="tile">
          <svg viewBox="0 0 32 32"><path d="M12 4h8v8h8v8h-8v8h-8v-8H4v-8h8z" fill="#fff"/></svg>
          <span>Public Health, Healthcare Healthcare IT</span>
        </div>
        <div class="tile">
          <svg viewBox="0 0 32 32"><path d="M19 2 8 18h7l-3 12 12-17h-7z" fill="#fff"/></svg>
          <span>Energy, Renewable Energy</span>
        </div>
        <div class="tile">
          <svg viewBox="0 0 32 32" fill="none" stroke="#fff" stroke-width="1.6"><path d="M2 13 16 6l14 7-14 7z"/><path d="M8 16v6c4 3 12 3 16 0v-6"/><path d="M29 13v8"/></svg>
          <span>Education</span>
        </div>
      </div>
    </div>

    <div class="naics">
      <h3 class="section-title is-teal">NAICS Codes</h3>
      <div class="naics-bar">561210 &nbsp;•&nbsp; 561210 &nbsp;•&nbsp; 561210 &nbsp;•&nbsp; 561210 &nbsp;•&nbsp; 561210 &nbsp;•<br>561210 &nbsp;•&nbsp; 561210 &nbsp;•&nbsp; 561210 &nbsp;•&nbsp; 561210 &nbsp;•&nbsp; 561210 &nbsp;•</div>
    </div>

    <div class="company-info">
      <h3 class="section-title">Company Info</h3>
      <div class="id-row">
        <span><b>EIN Number</b> 47-2019385</span>
        <span><b>DUNS Number</b> 204518736</span>
        <span><b>CAGE Number</b> 7K2M4</span>
      </div>
    </div>
  </section>

</body>
</html>
```